Barefoot Bowls A5 Flyer

We require an A5 Flyer to promote Barefoot Bowls at Tallowby Lawn Club. We want to promote Barefoot Bowls as a fun activity for all ages, and various occasions. (Private Functions including Birthdays, Christmas, Bucks and Hens Parties, as well as Corporate Functions, and Fundraising / Charity groups). The design should be bright and colourful, and include images of coloured Barefoot Bowls, as well as a Jumping Castle (which we offer as an optional extra). Price is $10 per person for 2 hours, and includes Instructor and Equipment. Various Catering options available. For Bookings or Enquiries call Peter on 0472 316 554, or Sonia at the Club on 4917 2093. Club address is: 12-16 Hartwell Road, Tallowby NSW 2631.

```html
<!DOCTYPE html>
<html lang="en">
<head>
<meta charset="utf-8">
<title>Barefoot Bowls at Tallowby Lawn Club</title>
<link href="https://fonts.googleapis.com/css2?family=Titan+One&family=Signika:wght@600&family=Open+Sans:ital,wght@0,400;0,700;1,400;1,700&family=Oswald:wght@700&display=swap" rel="stylesheet">
<style>
  :root {
    --page-bg: #ececec;
    --deep: #1a0608;
    --red: #c8102e;
    --wine: #6e0a10;
    --orange: #e8551a;
    --yellow: #f7ee00;
    --gold: #f5cc14;
    --ink: #111;
    --body-ink: #2a0505;
    --white: #fff;
  }
  * { margin: 0; padding: 0; box-sizing: border-box; }
  html, body { width: 1200px; height: 1172px; overflow: hidden; background: var(--page-bg); }
  .flyer {
    position: absolute; left: 210px; top: 32px; width: 780px; height: 1108px; overflow: hidden;
    background:
      radial-gradient(ellipse 260px 240px at 300px 560px, rgba(247,200,20,.85), rgba(232,85,26,.6) 55%, transparent 100%),
      radial-gradient(ellipse 500px 420px at 420px 470px, var(--red), rgba(200,16,46,.4) 70%, transparent 100%),
      linear-gradient(180deg, var(--wine) 0%, #a80d1d 30%, #8a0a14 60%, var(--deep) 85%);
    font-family: "Open Sans", sans-serif;
  }
  .bowl { position: absolute; border-radius: 50%; }
  .bowl-top {
    left: 560px; top: 110px; width: 230px; height: 240px;
    background: radial-gradient(circle at 40% 35%, #3b2a0a, #1a0a06 55%, rgba(20,5,5,.9) 75%, transparent 100%);
    filter: blur(3px);
  }
  .bowl-bottom {
    left: -60px; top: 790px; width: 420px; height: 420px;
    background: radial-gradient(circle at 45% 40%, #4a4008, #1a1405 45%, #0a0503 75%);
  }
  .title {
    position: absolute; left: 58px; top: 95px; transform: rotate(-12deg); transform-origin: left top;
    font-family: "Titan One", sans-serif; font-size: 82px; line-height: 70px; text-transform: uppercase;
    color: var(--yellow); -webkit-text-stroke: 14px var(--ink); paint-order: stroke fill;
    letter-spacing: -1px;
  }
  .title span { display: block; }
  .intro {
    position: absolute; left: 188px; top: 422px; width: 570px;
    font-family: "Signika", sans-serif; font-weight: 600; font-size: 25px; line-height: 36.5px; color: var(--body-ink);
  }
  .intro span { display: block; }
  .castle {
    position: absolute; left: 308px; top: 730px; width: 130px; height: 118px; border-radius: 10px;
    background: linear-gradient(135deg, #f2c318, #d8231f 55%, #2a3f9a);
    border: 4px solid var(--white);
  }
  .offer {
    position: absolute; left: 419px; top: 702px; width: 250px; height: 147px;
    border: 1px solid var(--gold); border-radius: 6px; padding: 18px 0 0 25px;
    color: var(--white); font-weight: 700; font-size: 23.5px; line-height: 28px; text-transform: uppercase;
  }
  .price {
    position: absolute; left: 585px; top: 632px; width: 160px; height: 160px; border-radius: 50%;
    background: radial-gradient(circle at 35% 25%, #fbe676, var(--gold) 55%, #eec300);
    text-align: center; color: var(--ink);
  }
  .price-amount {
    display: block; margin-top: 22px; font-family: "Oswald", sans-serif; font-size: 68px; line-height: 70px;
    color: var(--red); letter-spacing: -2px;
  }
  .price-note { display: block; font-weight: 700; font-size: 14px; line-height: 14px; margin-top: -6px; }
  .includes {
    position: absolute; left: 421px; top: 860px; color: var(--white); font-size: 16px; line-height: 24px; letter-spacing: -.3px;
  }
  .bookings { position: absolute; left: 412px; top: 936px; color: var(--white); font-style: italic; }
  .bookings-lead { font-size: 18.5px; line-height: 26px; }
  .bookings-lines { font-weight: 700; font-size: 22.5px; line-height: 29px; letter-spacing: -.4px; }
  .rule { position: absolute; left: 411px; top: 1027px; width: 304px; height: 1px; background: rgba(255,255,255,.55); }
  .address { position: absolute; left: 411px; top: 1036px; color: var(--gold); font-size: 18.5px; line-height: 22px; letter-spacing: -.3px; }
</style>
</head>
<body>
  <main class="flyer">
    <div class="bowl bowl-top" role="img" aria-label="Blurred lawn bowl photo"></div>
    <div class="bowl bowl-bottom" role="img" aria-label="Close-up photo of a dark lawn bowl with engraved rings"></div>

    <h1 class="title">
      <span>Barefoot</span>
      <span>Bowls at</span>
      <span>Tallowby</span>
      <span>Lawn</span>
      <span>Club.</span>
    </h1>

    <p class="intro">
      <span style="padding-left:242px">Barefoot Bowls as a fun</span>
      <span style="padding-left:220px">activity for all ages, and</span>
      <span style="padding-left:225px">various occasions.</span>
      <span style="padding-left:123px">(Private Functions including Birthdays,</span>
      <span>Christmas, Bucks and Hens Parties,</span>
      <span>as well as Corporate Functions, and</span>
      <span style="padding-left:14px">Fundraising / Charity groups).</span>
    </p>

    <div class="castle" role="img" aria-label="Illustration of an inflatable jumping castle"></div>
    <div class="offer">Barefoot<br>Bowls,<br>as well as a<br>jumping castle</div>

    <div class="price">
      <span class="price-amount">$10</span>
      <span class="price-note">PER PERSON<br>FOR 2 HOURS</span>
    </div>

    <p class="includes">Includes Instructor and Equipment.<br>Various Catering options available.</p>

    <div class="bookings">
      <p class="bookings-lead">For Bookings or Enquiries call</p>
      <p class="bookings-lines">Peter - 0472 316 554 or<br>Sonia at the Club on 4917 2093.</p>
    </div>

    <div class="rule"></div>
    <p class="address">Club Address: 12-16 Hartwell Road,<br>Tallowby NSW 2631.</p>
  </main>
</body>
</html>
```